Refined Sweets Table & Vessel Rental Needs a logo & business card design

I need a logo design and a business card design for a new candy buffet company based in Melbourne called "Pearl Sweets Table & Vessel Rental"(but the & Jar Hire part to be in smaller font). We set up candy bars with a wide variety of custom themes or to the customer's preference, we also hire out the glass jars if the customer prefers to do it themselves. But i want the emphasis on the front of the business card to be about the Candy Buffet and the jar hire can be at the back of the card. I would like to see designs that use the tiffany blue, or black and gold. I would like to see elegance, class but quite simple.

Industry/Entity Type

Business

Font styles to use
Script

```html
<!DOCTYPE html>
<html lang="en">
<head>
<meta charset="utf-8">
<title>Pearl Sweets Table &amp; Vessel Rental – Business Cards</title>
<link rel="stylesheet" href="https://fonts.googleapis.com/css2?family=Catamaran:wght@400;500;600&display=swap">
<style>
  :root {
    --page: #ffffff;
    --ink-black: #1b1a1a;
    --gold: #f7a823;
    --teal: #1fa5ad;
    --pearl: #f2f2f2;
    --shadow: rgba(0, 0, 0, 0.22);
  }
  * { margin: 0; padding: 0; box-sizing: border-box; }
  html, body {
    width: 1200px;
    height: 848px;
    overflow: hidden;
    background: var(--page);
    font-family: "Catamaran", "Helvetica Neue", Arial, sans-serif;
  }
  .sheet {
    position: relative;
    width: 1200px;
    height: 848px;
  }
  .card {
    position: absolute;
    width: 540px;
    height: 298px;
    overflow: hidden;
    box-shadow: 0 0 6px var(--shadow);
  }
  .card--black { background: var(--ink-black); color: var(--gold); --accent: var(--gold); }
  .card--teal { background: var(--teal); color: var(--pearl); --accent: var(--pearl); }

  .card--left { left: 43px; }
  .card--right { left: 614px; }
  .card--front { top: 95px; }
  .card--back { top: 413px; }

  /* Front: wordmark */
  .brand {
    position: absolute;
    left: 105px;
    top: 79px;
    display: flex;
    flex-direction: column;
    align-items: flex-end;
    color: var(--accent);
    font-weight: 500;
  }
  .brand__name {
    font-size: 130px;
    line-height: 0.95;
    letter-spacing: 1px;
    padding-right: 40px;
  }
  .brand__tagline {
    font-size: 14.5px;
    line-height: 1;
    letter-spacing: 0.3px;
    white-space: nowrap;
  }

  /* Back: contact side */
  .contact__name {
    position: absolute;
    left: 28px;
    top: 20px;
    font-size: 24px;
    font-weight: 500;
    letter-spacing: 0.3px;
  }
  .contact__rule {
    position: absolute;
    left: 93px;
    top: 80px;
    width: 57px;
    height: 3px;
    background: var(--accent);
  }
  .contact__list {
    list-style: none;
    position: absolute;
    left: 28px;
    top: 114px;
    font-size: 14px;
    font-weight: 500;
    letter-spacing: 0.4px;
  }
  .contact__list li { height: 64px; line-height: 20px; }
  .card__stripe {
    position: absolute;
    inset: 0;
    width: 540px;
    height: 298px;
  }
</style>
</head>
<body>
<main class="sheet">

  <section class="card card--black card--front card--left" aria-label="Black and gold card front">
    <div class="brand">
      <span class="brand__name">Pearl</span>
      <span class="brand__tagline">sweets table &amp; vessel rental</span>
    </div>
  </section>

  <section class="card card--teal card--front card--right" aria-label="Teal card front">
    <div class="brand">
      <span class="brand__name">Pearl</span>
      <span class="brand__tagline">sweets table &amp; vessel rental</span>
    </div>
  </section>

  <section class="card card--black card--back card--left" aria-label="Black and gold card back">
    <h2 class="contact__name">Mrs. Lorem Ipsum</h2>
    <span class="contact__rule"></span>
    <ul class="contact__list">
      <li>TEL :</li>
      <li>EMAIL :</li>
      <li>FACEBOOK :</li>
    </ul>
    <svg class="card__stripe" viewBox="0 0 540 298" aria-hidden="true">
      <line x1="580" y1="106" x2="250" y2="314" stroke="var(--gold)" stroke-width="10"/>
    </svg>
  </section>

  <section class="card card--teal card--back card--right" aria-label="Teal card back">
    <h2 class="contact__name">Mrs. Lorem Ipsum</h2>
    <span class="contact__rule"></span>
    <ul class="contact__list">
      <li>TEL :</li>
      <li>EMAIL :</li>
      <li>FACEBOOK :</li>
    </ul>
    <svg class="card__stripe" viewBox="0 0 540 298" aria-hidden="true">
      <line x1="580" y1="106" x2="250" y2="314" stroke="var(--pearl)" stroke-width="10"/>
    </svg>
  </section>

</main>
</body>
</html>
```